Personal letterhead and stationary

I am looking for someone to design letterhead and stationary set for my personal use. I want something simple and timeless with a little bit of color. I like photography, computers and writing.

```html
<!DOCTYPE html>
<html lang="en">
<head>
<meta charset="utf-8">
<title>Personal Letterhead – Daniel Owen Harper</title>
<link rel="stylesheet" href="https://fonts.googleapis.com/css2?family=Arimo&family=Carlito&family=Questrial&display=swap">
<style>
  :root {
    --paper: #ffffff;
    --accent-red: #ef3232;
    --accent-yellow: #ffd700;
    --body-grey: #7a7a7a;
    --name-grey: #666666;
    --ink: #111111;
  }
  html, body {
    margin: 0;
    padding: 0;
    overflow: hidden;
    background: var(--paper);
  }
  .letterhead {
    position: relative;
    width: 848px;
    height: 1200px;
    background: var(--paper);
    overflow: hidden;
  }
  .edge-band {
    position: absolute;
    width: 26px;
    display: flex;
    flex-direction: column;
  }
  .edge-band span { display: block; height: 76px; }
  .edge-band .red { background: var(--accent-red); }
  .edge-band .yellow { background: var(--accent-yellow); }
  .edge-band--top { left: 0; top: 0; }
  .edge-band--bottom { right: 0; bottom: 0; }

  .letter-body {
    position: absolute;
    left: 64px;
    top: 56px;
    width: 720px;
    font-family: "Arimo", Arial, sans-serif;
    font-size: 17.6px;
    line-height: 34.3px;
    color: var(--body-grey);
    text-align: justify;
    hyphens: auto;
  }
  .letter-body p { margin: 0 0 34.3px; }

  .signature-mark {
    position: absolute;
    left: 652px;
    top: 816px;
    width: 132px;
    height: 76px;
    background: linear-gradient(90deg, #f4f4f4, #ececec);
    border-radius: 4px;
  }

  .sender-name {
    position: absolute;
    right: 64px;
    top: 896px;
    margin: 0;
    font-family: "Questrial", "Century Gothic", sans-serif;
    font-weight: 400;
    font-size: 61px;
    line-height: 1;
    color: var(--name-grey);
    white-space: nowrap;
  }

  .contact-list {
    position: absolute;
    right: 64px;
    top: 992px;
    margin: 0;
    padding: 0;
    list-style: none;
    font-family: "Carlito", Calibri, sans-serif;
    font-size: 19.5px;
    color: var(--ink);
  }
  .contact-list li {
    display: flex;
    justify-content: flex-end;
    align-items: center;
    height: 42.6px;
  }
  .contact-list .icon {
    width: 22px;
    height: 22px;
    margin-left: 13px;
    flex: none;
  }
</style>
</head>
<body>
<main class="letterhead">
  <div class="edge-band edge-band--top" aria-hidden="true">
    <span class="red"></span><span class="yellow"></span><span class="red"></span><span class="yellow"></span>
  </div>

  <section class="letter-body">
    <p>Lorem ipsum dolor sit amet, consectetur adipiscing elit. Integer ac neque ligula. Pellentesque bibendum, lorem sit amet pretium ultricies, odio purus faucibus eros, a scelerisque orci leo ac libero. Sed fringilla ultricies rutrum. Praesent lacus magna, pharetra eu convallis at, consectetur vitae libero. Praesent vel turpis sem. Donec feugiat ultrices molestie. Suspendisse aliquet nunc non neque fermentum eget ultrices mi scelerisque. Cras dapibus, metus quis malesuada sagittis, ante quam congue elit, eu consectetur mauris dui vitae arcu. Nunc tincidunt tellus quis tortor accumsan iaculis. Suspendisse placerat dolor ut ipsum consequat vel euismod enim cursus. Suspendisse venenatis posuere porttitor. Phasellus vulpu&shy;tate magna ac sem egestas nec ultrices felis faucibus.</p>
    <p>Fusce bibendum ante eu urna malesuada eu dapibus magna lobortis. Integer sed nisl at velit vestibulum elementum. Cras et diam turpis. Etiam dictum lobortis felis, eu pulvinar dolor tincidunt a. Proin tincidunt, sem sed dignissim ultricies, tellus dolor scelerisque enim, sed ultrices nunc ante vestibulum odio. Morbi luctus facili&shy;sis urna, non mattis nisi ullamcorper ornare. Pellentesque habitant morbi tristique senectus et netus et malesuada fames ac turpis egestas. Donec est velit, placerat in volutpat eget, consectetur a felis. Aenean in blandit ipsum. Integer sit amet rhoncus nibh. Aliquam fringilla vestibulum erat, in blandit mauris pretium nec. Vivamus elementum nunc at lectus tempor sit amet pulvinar elit dictum. Nam pulvinar mauris non felis hendrerit consequat.</p>
  </section>

  <div class="signature-mark" role="img" aria-label="Handwritten signature"></div>

  <h1 class="sender-name">Daniel Owen Harper</h1>

  <ul class="contact-list">
    <li>XXX, XXXX, Millbrook, AL, USA
      <svg class="icon" viewBox="0 0 22 22" aria-hidden="true">
        <path d="M11 1C6.8 1 4 4 4 7.8 4 12.5 11 21 11 21s7-8.5 7-13.2C18 4 15.2 1 11 1z" fill="var(--ink)"/>
        <circle cx="11" cy="7.8" r="2.6" fill="var(--paper)"/>
      </svg>
    </li>
    <li>+1 000 000 00000
      <svg class="icon" viewBox="0 0 22 22" aria-hidden="true">
        <rect x="0.5" y="0.5" width="21" height="21" rx="4" fill="var(--ink)"/>
        <path d="M7 4.5c-1.2.6-2 1.8-1.6 3.8.9 4 4.4 8.4 7.8 9.6 1.8.6 3-.1 3.6-1.1l-2.4-2.4c-.5.3-1 .5-1.5.3-1.5-.7-3.4-3.2-3.8-4.8-.1-.5.2-1 .6-1.3L7 4.5z" fill="var(--paper)"/>
      </svg>
    </li>
    <li>daniel@danielharper.com
      <svg class="icon" viewBox="0 0 22 22" aria-hidden="true">
        <rect x="1" y="4" width="20" height="14" fill="none" stroke="var(--ink)" stroke-width="1.5"/>
        <path d="M1 4l10 8 10-8M1 18l7.5-7M21 18l-7.5-7" fill="none" stroke="var(--ink)" stroke-width="1.5"/>
      </svg>
    </li>
    <li>www.danielharper.com
      <svg class="icon" viewBox="0 0 22 22" aria-hidden="true">
        <g fill="none" stroke="var(--ink)" stroke-width="1.4">
          <circle cx="11" cy="11" r="9.5"/>
          <ellipse cx="11" cy="11" rx="4.2" ry="9.5"/>
          <path d="M11 1.5v19M1.5 11h19M3 6h16M3 16h16"/>
        </g>
      </svg>
    </li>
  </ul>

  <div class="edge-band edge-band--bottom" aria-hidden="true">
    <span class="red"></span><span class="yellow"></span><span class="red"></span><span class="yellow"></span>
  </div>
</main>
</body>
</html>
```